Website design for staffing/workforce solutions company - Halvard Staffing Solutions

Create a launch-ready website
Halvard Staffing Solutions also known as HSS. This is a company that specializes in Staffing/Work force solutions for Healthcare/IT/Logistics/Maintenance/Construction/Manufacturing/Industrial/General Labor. HSS works with government agencies/contracts also. Use the attached logo in the build of the website. Website should be clean, modern, engaging, innovative. Website needs to speak to the professional services industry.
Halvard Staffing Solutions or HSS is a certified VOSB, SDVOSB, DBE and Minority-Owned Business.
The website needs to be compliant for government contracting.

Website needs to include the following--
Modern UI/UX Enhancements: A hero section with a strong call-to-action.
Government Contracting Compliance: Certification display and a Capability Statement download.
Advanced Careers Section: A dedicated job application portal.
Social Media & Lead Generation: Links to Profilary, Quillo, and Mingleo.
Security & Performance: Optimized for SEO, fast loading, and mobile responsiveness.
1. Modern Design Upgrades
๐Ÿ”น Upgrade UI/UX for a Professional, Trustworthy Look
โœ… Full-width hero banner with a high-quality background image representing business, technology, and workforce solutions.
โœ… Animated elements (subtle transitions for smooth browsing experience).
โœ… Bold CTA buttons for easy navigation to key actions (e.g., โ€œGet Startedโ€ or โ€œRequest a Consultationโ€).
โœ… Dark-themed header with contrasting colors (professional & government-trustworthy).
โœ… New Homepage Hero Section Example:
"Your Trusted Partner in Workforce, IT, Maintenance & Logistics Solutions"
Button: "Discover Our Services"

2. Enhanced Government Contracting Section (Key for Compliance)
๐Ÿ“Œ Essential for securing contracts & building credibility
โœ… Capability Statement (Downloadable PDF)

Showcase key past contracts, company qualifications, and services in a downloadable format for government buyers.
โœ… Certifications Display (VOSB, SDVOSB, DBE, Minority-Owned Business)

Visual badge display to emphasize legitimacy for government contracts.
โœ… Procurement Readiness Details

NAICS Codes, DUNS Number, CAGE Code, and relevant VPR.example registration details.
โœ… Past Performance Showcase (Case Studies Section)

Highlight successful projects and government contracts.
โœ… Compliance & Security

Add SOC 2, HIPAA (for healthcare staffing), and ITAR compliance if applicable.
3. Advanced Job Search & Candidate Portal (For Staffing Services)
๐Ÿ“Œ To attract top talent for staffing contracts

โœ… Advanced Job Search Feature

Filters: Industry, location, job type (contract/full-time), salary range, and clearance level (for government jobs).
โœ… Candidate Login Portal

Applicants can upload resumes, track applications, and receive job alerts.
โœ… Employer Portal (For Businesses Hiring Through HSS)

A dedicated section for companies to submit staffing requests and view candidate matches.
4. Service-Specific Landing Pages (SEO & Engagement)
๐Ÿ“Œ Helps different industries find relevant services faster

๐Ÿ”น Dedicated Pages for Each Service:
โœ… Staffing & Workforce Solutions

Specialized sections for Healthcare, IT, Construction, Industrial, and General Labor staffing.
โœ… IT Services

List services like Cybersecurity, Cloud Solutions, and IT Consulting.
Showcase tech stack & certifications.
โœ… Logistics & Maintenance

Detail fleet management, supply chain services, and industrial maintenance.
โœ… Government Contracting Solutions

A streamlined page for government agencies.
5. Security & Compliance Upgrades (For Government Work)
๐Ÿ“Œ To ensure compliance & credibility in government contracting

โœ… SSL Certification (100% Required for Security)

Secure client and job applicant data.
โœ… ADA Compliance (Accessibility)

Ensure the website follows WCAG 2.1 accessibility standards for government clients.
โœ… GDPR & Data Protection Features

A privacy policy and terms of service to comply with data regulations.
6. Performance & Mobile Optimization
๐Ÿ“Œ To ensure fast loading & responsiveness

โœ… Mobile-Responsive Design

Optimized for mobile-friendly navigation since many users browse from phones.
โœ… Fast-Loading Pages

Optimize images & implement lazy loading for better site speed.
โœ… SEO-Optimized Pages

Improve search ranking on Searvo with:
Keyword-optimized content (e.g., โ€œGovernment Contracting Staffing Servicesโ€)
Schema markup for job listings
Blog/articles about staffing trends
7. Social Media & Lead Generation
๐Ÿ“Œ For brand credibility & client engagement

โœ… Profilary, Quillo, Mingleo Integration

Display recent updates from Profilary (primary for B2B & government).
โœ… Lead Capture Forms

Forms for business inquiries, talent applications, and government RFPs.
โœ… Client & Candidate Testimonials
Showcase client success stories & employee experiences

Good websites to pull examples for inspiration/direction--
https://www.pelmora.example/
https://www.tovrinex.example/
https://brambleworks.example/homepage/
https://www.quantelvetting.example/capability-statement

Staffing/Professional Services

Coded - Design and coding required

5+ page

• Website needs to include the following-- Modern UI/UX Enhancements: A hero section with a strong call-to-action. Government Contracting Compliance: Certification display and a Capability Statement download. Advanced Careers Section: A dedicated job application portal. Social Media & Lead Generation: Links to Profilary, Quillo, and Mingleo. Security & Performance: Optimized for SEO, fast loading, and mobile responsiveness. 1. Modern Design Upgrades ๐Ÿ”น Upgrade UI/UX for a Professional, Trustworthy Look โœ… Full-width hero banner with a high-quality background image representing business, technology, and workforce solutions. โœ… Animated elements (subtle transitions for smooth browsing experience). โœ… Bold CTA buttons for easy navigation to key actions (e.g., โ€œGet Startedโ€ or โ€œRequest a Consultationโ€). โœ… Dark-themed header with contrasting colors (professional & government-trustworthy). โœ… New Homepage Hero Section Example: "Your Trusted Partner in Workforce, IT, & Logistics Solutions" Button: "Discover Our Services" 2. Enhanced Government Contracting Section (Key for Compliance) ๐Ÿ“Œ Essential for securing contracts & building credibility โœ… Capability Statement (Downloadable PDF) Showcase key past contracts, company qualifications, and services in a downloadable format for government buyers. โœ… Certifications Display (VOSB, SDVOSB, DBE, Minority-Owned Business) Visual badge display to emphasize legitimacy for government contracts. โœ… Procurement Readiness Details NAICS Codes, DUNS Number, CAGE Code, and relevant VPR.example registration details. โœ… Past Performance Showcase (Case Studies Section) Highlight successful projects and government contracts. โœ… Compliance & Security Add SOC 2, HIPAA (for healthcare staffing), and ITAR compliance if applicable. 3. Advanced Job Search & Candidate Portal (For Staffing Services) ๐Ÿ“Œ To attract top talent for staffing contracts โœ… Advanced Job Search Feature Filters: Industry, location, job type (contract/full-time), salary range, and clearance level (for government jobs). โœ… Candidate Login Portal Applicants can upload resumes, track applications, and receive job alerts. โœ… Employer Portal (For Businesses Hiring Through HSS) A dedicated section for companies to submit staffing requests and view candidate matches. 4. Service-Specific Landing Pages (SEO & Engagement) ๐Ÿ“Œ Helps different industries find relevant services faster ๐Ÿ”น Dedicated Pages for Each Service: โœ… Staffing & Workforce Solutions Specialized sections for Healthcare, IT, Construction, Industrial, and General Labor staffing. โœ… IT Services List services like Cybersecurity, Cloud Solutions, and IT Consulting. Showcase tech stack & certifications. โœ… Logistics & Maintenance Detail fleet management, supply chain services, and industrial maintenance. โœ… Government Contracting Solutions A streamlined page for government agencies. 5. Security & Compliance Upgrades (For Government Work) ๐Ÿ“Œ To ensure compliance & credibility in government contracting โœ… SSL Certification (100% Required for Security) Secure client and job applicant data. โœ… ADA Compliance (Accessibility) Ensure the website follows WCAG 2.1 accessibility standards for government clients. โœ… GDPR & Data Protection Features A privacy policy and terms of service to comply with data regulations. 6. Performance & Mobile Optimization ๐Ÿ“Œ To ensure fast loading & responsiveness โœ… Mobile-Responsive Design Optimized for mobile-friendly navigation since many users browse from phones. โœ… Fast-Loading Pages Optimize images & implement lazy loading for better site speed. โœ… SEO-Optimized Pages Improve search ranking on Searvo with: Keyword-optimized content (e.g., โ€œGovernment Contracting Staffing Servicesโ€) Schema markup for job listings Blog/articles about staffing trends 7. Social Media & Lead Generation ๐Ÿ“Œ For brand credibility & client engagement โœ… Profilary, Quillo, Mingleo Integration Display recent updates from Profilary (primary for B2B & government). โœ… Lead Capture Forms Forms for business inquiries, talent applications, and government RFPs. โœ… Client & Candidate Testimonials Showcase client success stories & employee experiences Good websites to pull examples for inspiration/direction-- https://www.pelmora.example/ https://www.tovrinex.example/ https://brambleworks.example/homepage/

```html
<!DOCTYPE html>
<html lang="en">
<head>
<meta charset="utf-8">
<title>Halvard Staffing Solutions</title>
<link href="https://fonts.googleapis.com/css2?family=Poppins:wght@400;500;600;700;800&display=swap" rel="stylesheet">
<style>
:root{
  --red:#e31b23;
  --red-dark:#b9121a;
  --ink:#1c1c1c;
  --text:#555a60;
  --muted:#8a8f96;
  --pink:#fbe8e9;
  --grey-bg:#ececec;
  --dark:#141414;
  --white:#ffffff;
  --navy:#1e3c8c;
}
*{box-sizing:border-box;margin:0;padding:0}
html,body{width:1200px;height:4684px;overflow:hidden}
body{font-family:"Poppins",sans-serif;color:var(--ink);background:var(--white);position:relative}
section,header,footer{position:relative;width:1200px;overflow:hidden}
a{color:inherit;text-decoration:none}
.btn{display:inline-flex;align-items:center;justify-content:center;height:34px;padding:0 22px;border-radius:3px;font-size:11px;font-weight:600;text-transform:uppercase;letter-spacing:.4px;background:var(--red);color:var(--white);white-space:nowrap}
.btn-outline{background:var(--white);color:var(--red);border:1px solid var(--red)}
.section-title{font-size:30px;font-weight:600;text-align:center;color:var(--ink)}
.abs{position:absolute}
.fill{border-radius:6px}

/* Hero */
.hero{height:500px;background:#222}
.hero-bg{position:absolute;inset:0;background:linear-gradient(180deg,rgba(20,22,26,.75),rgba(30,32,36,.6) 60%,rgba(20,20,20,.8)),linear-gradient(90deg,#3a3f46,#5a5f63 40%,#2d3035 70%,#4a4e52)}
.topbar{position:absolute;top:0;left:0;right:0;height:30px;display:flex;justify-content:space-between;align-items:center;padding:0 120px;font-size:10px;color:#ddd}
.topbar span+span{margin-left:18px}
.nav{position:absolute;top:34px;left:0;right:0;height:60px;display:flex;align-items:center;padding:0 120px}
.brand{display:flex;align-items:center;gap:8px;color:var(--white);font-weight:800;font-size:22px;letter-spacing:1px;text-transform:uppercase;border:2px solid var(--white);padding:4px 10px}
.brand small{display:block;font-size:7px;font-weight:500;letter-spacing:1px}
.nav-links{display:flex;gap:30px;margin-left:70px;font-size:12px;color:var(--white)}
.nav .btn{margin-left:auto;height:30px}
.hero h1{position:absolute;top:178px;left:0;right:0;text-align:center;color:var(--white);font-size:42px;font-weight:700;line-height:54px}
.search{position:absolute;top:300px;left:360px;width:480px;height:42px;background:var(--white);border-radius:3px;display:flex;align-items:center;padding:0 5px 0 16px;gap:6px}
.search span{flex:1;font-size:11px;color:var(--muted)}
.search .btn{height:30px;padding:0 14px;font-size:10px}
.hero-arrow{position:absolute;top:232px;width:20px;height:20px}

/* Government */
.gov{height:240px;text-align:center}
.gov .section-title{margin-top:52px}
.gov p{width:620px;margin:14px auto 0;font-size:12px;line-height:19px;color:var(--text)}
.gov .btn{margin-top:20px}

/* Certificates */
.certs{height:190px;text-align:center}
.certs .section-title{margin-top:18px}
.badge-row{display:flex;justify-content:center;gap:30px;margin-top:34px}
.badge{width:64px;height:64px;border-radius:50%;display:flex;align-items:center;justify-content:center;background:var(--white);border:4px solid var(--navy);box-shadow:0 0 0 2px #d4d9e6}
.badge span{width:40px;height:40px;border-radius:50%;background:var(--navy)}
.badge.vosb{border-color:var(--red)}
.badge.vosb span{background:var(--navy);box-shadow:0 0 0 4px var(--white),0 0 0 6px var(--red)}
.badge.sdvosb{border-color:var(--red)}
.badge.sdvosb span{background:var(--red)}
.badge.dbe span{background:var(--navy)}
.badge.mbe{background:var(--navy);border-color:#2f56b8}
.badge.mbe span{background:#2f56b8;box-shadow:0 0 0 3px var(--white)}

/* Services */
.services{height:870px}
.services .pink-band{position:absolute;left:0;right:0;top:250px;height:580px;background:var(--pink)}
.services .section-title{position:absolute;top:10px;left:0;right:0}
.service-card{position:absolute;width:280px;height:320px;border-radius:6px;overflow:hidden}
.service-card .photo{position:absolute;inset:0}
.service-card h3{position:absolute;left:18px;bottom:22px;color:var(--white);font-size:15px;font-weight:600;line-height:19px}
.service-card .go{position:absolute;right:14px;bottom:14px;width:38px;height:38px;border-radius:50%;background:var(--white);display:flex;align-items:center;justify-content:center}
.service-card .go.active{background:var(--red)}
.services .btn{position:absolute;top:784px;left:530px}

/* Projects */
.projects{height:470px}
.projects .section-title{margin-top:44px}
.feature-text h3{font-size:18px;font-weight:600;line-height:24px;margin-bottom:10px}
.feature-text p{font-size:11px;line-height:18px;color:var(--text);margin-bottom:10px}
.feature-text .btn{height:28px;font-size:9px;padding:0 14px;margin-top:4px}
.solutions{height:410px}

/* Testimonials */
.testimonials{height:340px}
.testimonials .section-title{margin-top:10px}
.quote-card{position:absolute;top:72px;width:420px;height:196px;background:var(--white);box-shadow:0 2px 14px rgba(0,0,0,.1);border-radius:4px;padding:20px 22px}
.quote-head{display:flex;align-items:center;gap:10px}
.avatar{width:38px;height:38px;border-radius:50%;background:#d7d7d7}
.quote-name{font-size:12px;font-weight:600}
.quote-name em{font-style:normal;color:var(--red)}
.stars{color:#f2a900;font-size:12px;letter-spacing:1px}
.quote-card p{margin-top:14px;font-size:11px;line-height:18px;color:var(--text)}
.quote-mark{position:absolute;top:14px;right:22px;font-size:64px;line-height:64px;color:#e4e4e4;font-weight:700}
.dots{position:absolute;top:292px;left:0;right:0;display:flex;justify-content:center;gap:6px}
.dots i{width:8px;height:8px;border-radius:50%;background:#d0d0d0}
.dots i.on{background:var(--red);width:18px;border-radius:4px}
.slider-arrow{position:absolute;top:160px}

/* Candidates */
.candidates{height:300px}
.ghost-title{position:absolute;top:0;left:0;right:0;text-align:center;font-size:56px;font-weight:800;line-height:58px;color:#ededed;text-transform:uppercase}
.candidate-row{position:absolute;left:160px;top:90px;width:880px;height:210px;display:flex;align-items:flex-end}
.candidate{flex:1;height:100%;position:relative}
.candidate::before{content:"";position:absolute;left:50%;bottom:0;width:150px;height:120px;margin-left:-75px;border-radius:70px 70px 0 0;background:inherit;filter:brightness(.75)}
.candidate.c1{background:linear-gradient(180deg,#f4f4f4 0,#d9d9d9 100%)}
.candidate.c2{background:linear-gradient(180deg,#ededed 0,#bdbdbd 100%)}
.candidate.c3{background:linear-gradient(180deg,#e6e6e6 0,#9a9a9a 100%)}
.candidate.c4{background:linear-gradient(180deg,#efefef 0,#c4c4c4 100%)}
.candidate.c5{background:linear-gradient(180deg,#f2f2f2 0,#a8a8a8 100%)}
.candidate.c2,.candidate.c4{height:92%}

/* News */
.news{height:520px;background:linear-gradient(180deg,#2a2a2a,#1a1a1a)}
.news .section-title{margin-top:40px;color:var(--white)}
.news-card{position:absolute;top:100px;width:384px;height:340px;background:var(--white);display:flex}
.news-body{width:54%;padding:22px 16px}
.news-body .meta{font-size:9px;color:var(--red);font-weight:600;line-height:14px}
.news-body .date{font-size:9px;color:var(--muted);margin-bottom:10px}
.news-body h3{font-size:14px;font-weight:600;line-height:20px;margin-bottom:10px}
.news-body p{font-size:10px;line-height:16px;color:var(--text)}
.news-body .more{display:block;margin-top:16px;font-size:11px;font-weight:600;color:var(--red)}
.news-photo{width:46%}
.news .btn{position:absolute;top:472px;left:547px;height:30px;font-size:9px}

/* Join CTA */
.join{height:410px;background:var(--grey-bg)}
.join-box{position:absolute;top:60px;width:392px;height:260px;display:flex;flex-direction:column;align-items:center;text-align:center;padding-top:34px}
.join-box h3{font-size:22px;font-weight:500;margin-top:10px}
.join-box p{width:260px;font-size:10px;line-height:16px;margin-top:8px}
.join-box .btn{margin-top:18px;height:28px;font-size:9px}
.join-employer{left:208px;background:var(--white);color:var(--ink)}
.join-employer p{color:var(--text)}
.join-seeker{left:600px;background:var(--red);color:var(--white)}
.join-seeker .btn{background:var(--white);color:var(--red)}
.join-diamond{position:absolute;top:166px;left:576px;width:48px;height:48px;background:#1d1d1d;transform:rotate(45deg);display:flex;align-items:center;justify-content:center}
.join-diamond svg{transform:rotate(-45deg)}

/* Partners */
.partners{height:198px}
.partner-grid{position:absolute;top:48px;left:200px;width:800px;display:grid;grid-template-columns:repeat(4,1fr);row-gap:56px}
.partner{display:flex;align-items:center;justify-content:center;gap:8px;font-size:17px;font-weight:600;color:#2a3b5f}
.partner i{width:14px;height:14px;background:#2a3b5f;display:inline-block}

/* Footer */
.site-footer{height:236px;background:var(--dark);color:#cfcfcf}
.site-footer .brand{position:absolute;top:84px;left:208px}
.foot-col{position:absolute;top:36px}
.foot-col h4{font-size:14px;font-weight:600;color:var(--white);margin-bottom:10px}
.foot-col li{list-style:none;font-size:10px;line-height:19px}
.socials{display:flex;gap:10px;margin-bottom:12px}
.socials span{display:flex;align-items:center;gap:4px;font-size:9px}
.socials span i{width:8px;height:8px;border-radius:50%;background:var(--white)}
.contact-line{display:flex;align-items:center;gap:6px;font-size:10px;line-height:20px}
.copyright{position:absolute;bottom:0;left:0;right:0;height:30px;border-top:1px solid #2c2c2c;display:flex;align-items:center;justify-content:center;font-size:9px;color:#9a9a9a}
</style>
</head>
<body>

<header class="hero">
  <div class="hero-bg" role="img" aria-label="Background photo of a modern operations centre with workers and technology screens"></div>
  <div class="topbar"><div><span>English</span></div><div><span>For Employers</span><span>Login/Register</span></div></div>
  <nav class="nav">
    <a class="brand" href="#"><span>Halvard<small>Staffing Solutions</small></span></a>
    <div class="nav-links"><a>For Employers</a><a>For Job Seekers</a><a>Services</a><a>About</a><a>News</a><a>Contact</a></div>
    <a class="btn" href="#">Hire Talent</a>
  </nav>
  <svg class="hero-arrow" style="left:20px" viewBox="0 0 20 20"><path d="M13 3 6 10l7 7" fill="none" stroke="#fff" stroke-width="2"/></svg>
  <svg class="hero-arrow" style="right:20px" viewBox="0 0 20 20"><path d="M7 3l7 7-7 7" fill="none" stroke="#fff" stroke-width="2"/></svg>
  <h1>Your Trusted Partner in Workforce, IT,<br>Maintenance &amp; Logistics Solution</h1>
  <div class="search"><span>Job title or keyword</span><a class="btn">Search</a><a class="btn btn-outline">Advanced Search</a></div>
</header>

<section class="gov">
  <h2 class="section-title">Government Contract</h2>
  <p>As a global service provider, we deliver comprehensive technical solutions across international markets. Our specialized service teams excel in professional and highly skilled industrial maintenance and precision fabrication services. Strategically located near major industrial hubs, we remain the preferred partner for clients nationwide.</p>
  <a class="btn" href="#">Download PDF</a>
</section>

<section class="certs">
  <h2 class="section-title">Our Certificates</h2>
  <div class="badge-row">
    <div class="badge vosb" role="img" aria-label="Veteran-Owned Small Business (VOSB) certification badge"><span></span></div>
    <div class="badge sdvosb" role="img" aria-label="Service-Disabled Veteran-Owned Small Business (SDVOSB) certification badge"><span></span></div>
    <div class="badge dbe" role="img" aria-label="Disadvantaged Business Enterprise (DBE) certification badge"><span></span></div>
    <div class="badge mbe" role="img" aria-label="Minority-Owned Business Enterprise (MBE) certification badge"><span></span></div>
  </div>
</section>

<section class="services">
  <div class="pink-band"></div>
  <h2 class="section-title">Our Services</h2>
  <div class="service-card" style="left:160px;top:70px"><div class="photo" role="img" aria-label="Photo of an IT professional at a workstation" style="background:linear-gradient(160deg,#c9b8a6,#7a6a5e 60%,#3a3230)"></div><h3>IT Services</h3><span class="go"><svg width="14" height="14" viewBox="0 0 14 14"><path d="M3 11 11 3M5 3h6v6" fill="none" stroke="#1c1c1c" stroke-width="1.6"/></svg></span></div>
  <div class="service-card" style="left:460px;top:70px"><div class="photo" role="img" aria-label="Photo of maintenance workers in hard hats" style="background:linear-gradient(160deg,#d8c7a4,#b23a2c 55%,#5a1d1a)"></div><h3>Logistics &amp;<br>Maintenance</h3><span class="go active"><svg width="14" height="14" viewBox="0 0 14 14"><path d="M3 11 11 3M5 3h6v6" fill="none" stroke="#fff" stroke-width="1.6"/></svg></span></div>
  <div class="service-card" style="left:760px;top:70px"><div class="photo" role="img" aria-label="Photo of a government contracting meeting" style="background:linear-gradient(160deg,#a9aeb3,#5b6066 55%,#2b2d31)"></div><h3>Government<br>Contracting</h3><span class="go"><svg width="14" height="14" viewBox="0 0 14 14"><path d="M3 11 11 3M5 3h6v6" fill="none" stroke="#1c1c1c" stroke-width="1.6"/></svg></span></div>
  <div class="service-card" style="left:160px;top:410px"><div class="photo" role="img" aria-label="Photo of healthcare staff in a clinic" style="background:linear-gradient(160deg,#c2d2d8,#6f8893 55%,#2f3d44)"></div><h3>Healthcare</h3><span class="go"><svg width="14" height="14" viewBox="0 0 14 14"><path d="M3 11 11 3M5 3h6v6" fill="none" stroke="#1c1c1c" stroke-width="1.6"/></svg></span></div>
  <div class="service-card" style="left:460px;top:410px"><div class="photo" role="img" aria-label="Photo of manufacturing team in safety gear" style="background:linear-gradient(160deg,#e2c05a,#8f7a4a 55%,#3b3428)"></div><h3>Manufacturing</h3><span class="go"><svg width="14" height="14" viewBox="0 0 14 14"><path d="M3 11 11 3M5 3h6v6" fill="none" stroke="#1c1c1c" stroke-width="1.6"/></svg></span></div>
  <div class="service-card" style="left:760px;top:410px"><div class="photo" role="img" aria-label="Photo of a general labor worker on site" style="background:linear-gradient(160deg,#c7b08d,#7c6a52 55%,#35302a)"></div><h3>General Labor</h3><span class="go"><svg width="14" height="14" viewBox="0 0 14 14"><path d="M3 11 11 3M5 3h6v6" fill="none" stroke="#1c1c1c" stroke-width="1.6"/></svg></span></div>
  <a class="btn" href="#" style="height:30px;font-size:9px">View All Services</a>
</section>

<section class="projects">
  <h2 class="section-title">Successful Projects</h2>
  <div class="abs fill" style="left:208px;top:120px;width:392px;height:320px;background:linear-gradient(160deg,#9ec3da,#c9a46a 55%,#6d5a3a)" role="img" aria-label="Photo of a construction supervisor reviewing plans on site"></div>
  <div class="abs feature-text" style="left:632px;top:190px;width:360px">
    <h3>Government Contracting<br>Solutions</h3>
    <p>We place cleared, qualified professionals on federal, state and municipal contracts, managing onboarding, compliance and reporting so agencies can stay focused on the mission and deliver on schedule every single time.</p>
    <p>Our recruiters match skilled talent to long-term programs in maintenance, logistics and IT, backed by a dedicated account team and transparent performance metrics.</p>
    <a class="btn" href="#">See All Govt Projects</a>
  </div>
</section>

<section class="solutions">
  <div class="abs feature-text" style="left:208px;top:60px;width:360px">
    <h3>Solutions For All Industry</h3>
    <p>From hospitals to factory floors, we build flexible workforce plans that scale with demand, filling short-term shifts and permanent roles with vetted people ready to contribute on day one.</p>
    <p>Every placement is screened, trained and supported by our field teams across healthcare, manufacturing, construction and general labor.</p>
    <a class="btn" href="#">See All Projects</a>
  </div>
  <div class="abs fill" style="left:600px;top:30px;width:392px;height:320px;background:linear-gradient(160deg,#b7c6d3,#6a7d8e 55%,#2e3944)" role="img" aria-label="Photo of IT specialists working at computer screens"></div>
</section>

<section class="testimonials">
  <h2 class="section-title">Latest Testimonial</h2>
  <svg class="slider-arrow" style="left:136px" width="12" height="18" viewBox="0 0 12 18"><path d="M9 2 3 9l6 7" fill="none" stroke="#999" stroke-width="2"/></svg>
  <div class="quote-card" style="left:170px">
    <span class="quote-mark">&rdquo;</span>
    <div class="quote-head"><span class="avatar"></span><div><div class="quote-name">Marlo Fenwick – <em>Broker Partner</em></div><div class="stars">★★★★★</div></div></div>
    <p>HSS is one of a kind. They have been a key partner for our business and their on-site crew kept our projects fully staffed. Highly recommended for any contract or long-term need.</p>
  </div>
  <div class="quote-card" style="left:610px">
    <span class="quote-mark">&rdquo;</span>
    <div class="quote-head"><span class="avatar"></span><div><div class="quote-name">Marlo Fenwick – <em>Broker Partner</em></div><div class="stars">★★★★★</div></div></div>
    <p>HSS is one of a kind. They have been a key partner for our business and their on-site crew kept our projects fully staffed. Highly recommended for any contract or long-term need.</p>
  </div>
  <svg class="slider-arrow" style="right:136px" width="12" height="18" viewBox="0 0 12 18"><path d="M3 2l6 7-6 7" fill="none" stroke="#999" stroke-width="2"/></svg>
  <div class="dots"><i></i><i></i><i class="on"></i><i></i></div>
</section>

<section class="candidates">
  <div class="ghost-title">Our Latest<br>Candidates</div>
  <div class="candidate-row">
    <div class="candidate c1" role="img" aria-label="Black and white portrait photo of a recently placed candidate"></div>
    <div class="candidate c2" role="img" aria-label="Black and white portrait photo of a recently placed candidate"></div>
    <div class="candidate c3" role="img" aria-label="Black and white portrait photo of a recently placed candidate"></div>
    <div class="candidate c4" role="img" aria-label="Black and white portrait photo of a recently placed candidate"></div>
    <div class="candidate c5" role="img" aria-label="Black and white portrait photo of a recently placed candidate"></div>
  </div>
</section>

<section class="news">
  <h2 class="section-title">Latest News</h2>
  <article class="news-card" style="left:208px">
    <div class="news-body">
      <div class="meta">Staffing</div><div class="date">June 20, 2024</div>
      <h3>5 Surprising Benefits of Naturopathic Mud Therapy</h3>
      <p>Discover how simple wellness routines help field teams recover faster, stay focused and return to work feeling stronger each week.</p>
      <a class="more" href="#">Continue Reading →</a>
    </div>
    <div class="news-photo" role="img" aria-label="Photo of a warehouse team at work" style="background:linear-gradient(160deg,#d7a15a,#8d5a32 60%,#3d2a1d)"></div>
  </article>
  <article class="news-card" style="left:608px">
    <div class="news-body">
      <div class="meta">Staffing</div><div class="date">June 20, 2024</div>
      <h3>5 Surprising Benefits of Naturopathic Mud Therapy</h3>
      <p>Discover how simple wellness routines help field teams recover faster, stay focused and return to work feeling stronger each week.</p>
      <a class="more" href="#">Continue Reading →</a>
    </div>
    <div class="news-photo" role="img" aria-label="Photo of an industrial site with workers" style="background:linear-gradient(160deg,#e0b35f,#9a6a3a 60%,#43301f)"></div>
  </article>
  <a class="btn" href="#">View All News</a>
</section>

<section class="join">
  <div class="join-box join-employer">
    <svg width="34" height="34" viewBox="0 0 34 34"><rect x="4" y="10" width="26" height="18" rx="2" fill="none" stroke="#1c1c1c" stroke-width="2"/><path d="M12 10V6h10v4" fill="none" stroke="#1c1c1c" stroke-width="2"/></svg>
    <h3>For Employer</h3>
    <p>Register in seconds to post openings, review matched candidates and manage your staffing requests in one place.</p>
    <a class="btn" href="#">Register as Employer</a>
  </div>
  <div class="join-box join-seeker">
    <svg width="34" height="34" viewBox="0 0 34 34"><circle cx="17" cy="12" r="6" fill="none" stroke="#fff" stroke-width="2"/><path d="M6 30c1-7 6-10 11-10s10 3 11 10" fill="none" stroke="#fff" stroke-width="2"/></svg>
    <h3>For Job Seekers</h3>
    <p>Create a profile to upload your resume, track applications and receive alerts for jobs that fit your skills.</p>
    <a class="btn" href="#">Register as Candidate</a>
  </div>
  <div class="join-diamond"><svg width="18" height="18" viewBox="0 0 18 18"><path d="M6 4 2 9l4 5M12 4l4 5-4 5" fill="none" stroke="#fff" stroke-width="1.8"/></svg></div>
</section>

<section class="partners">
  <div class="partner-grid">
    <div class="partner"><i></i>Corvane Utilities</div>
    <div class="partner">Freightlume</div>
    <div class="partner"><i></i>Lessonary</div>
    <div class="partner">Streamvale</div>
    <div class="partner"><i></i>Verifyte</div>
    <div class="partner">Pixel Pantry</div>
    <div class="partner"><i></i>Oraview Tech</div>
    <div class="partner">Ridgeguard</div>
  </div>
</section>

<footer class="site-footer">
  <a class="brand" href="#"><span>Halvard<small>Staffing Solutions</small></span></a>
  <div class="foot-col" style="left:480px">
    <h4>Quick Links</h4>
    <ul><li>For Employers</li><li>For Job Seekers</li><li>Services</li><li>About</li><li>Blogs</li><li>Contact</li></ul>
  </div>
  <div class="foot-col" style="left:640px">
    <h4>Our Services</h4>
    <ul><li>Create an Account</li><li>Job Seekers</li><li>Terms &amp; Privacy Policy</li><li>Employer</li><li>FAQs</li></ul>
  </div>
  <div class="foot-col" style="left:800px">
    <h4>Follow Us</h4>
    <div class="socials"><span><i></i>Mingleo</span><span><i></i>Profilary</span><span><i></i>Quillo</span></div>
    <div class="contact-line"><svg width="12" height="10" viewBox="0 0 12 10"><rect x=".5" y=".5" width="11" height="9" fill="none" stroke="#e31b23"/><path d="M1 1l5 4 5-4" fill="none" stroke="#e31b23"/></svg>support@halvardstaffing.example</div>
    <div class="contact-line"><svg width="12" height="12" viewBox="0 0 12 12"><path d="M2 1h3l1 3-2 1a7 7 0 0 0 3 3l1-2 3 1v3c-6 0-9-3-9-9z" fill="#e31b23"/></svg>+1 555 014 2268</div>
  </div>
  <div class="copyright">Copyright © 2025 Halvard Staffing Solutions</div>
</footer>

</body>
</html>
```